Business card design - landscaping industry

Hello! We are very creative when it comes to landscape design but when it comes to designing business cards - not so much. We could use some help to come up with a design which is professional but fun. We are based in Grand Rapids, MI and work with high end properties for new landscape design and install. We are looking to have a template made for business card for a couple of us on staff.

You can get the flavor of our color scheme from our attached logo. We probably would want to highlight the green but also include some of the blue maybe.

Target Market(s)

We work with residential homeowners here in West Michigan. Very nice people by and large.

Industry/Entity Type

Landscaping

Contact Information for Business Card

The card should be standard size with round edges maybe?

Font styles to use
Serif
Sans Serif
Decorative

Requirements
Must have
• Must haves:
• 1. Address: 4817 Birchwell Meadow Lane SE, Grand Rapids, Michigan 49582
• 2. Phone: 616.555.0187
• 3. Email: company@larkhollowyard.com
• 4. URL: www.larkhollowyard.com
• 5. Names/Titles: (1) Dennis Harlow, President (2) Tomas Belvin, Director of Field Services
Nice to have
• On the back side of the card, we are thinking it would make sense to have a short listing of services offered...
• Landscape design & installation, Professional lawn maintenance, Spring & fall leaf cleanup, Irrigation system installation & maintenance, Snowplowing, Fertilizer & weed control, Tree maintenance and removal, Landscape bed maintenance
Should not have
• Our hope is that the design won't be too ostentatious. We are looking for professional and attractive.

```html
<!DOCTYPE html>
<html lang="en">
<head>
<meta charset="utf-8">
<title>Lark Hollow Yard – Business Card</title>
<link rel="stylesheet" href="https://fonts.googleapis.com/css2?family=Cinzel:wght@400;600&family=Work+Sans:wght@400&family=Roboto+Condensed:wght@400;700&display=swap">
<style>
  :root {
    --backdrop: #5e4730;
    --card-white: #ffffff;
    --card-dark: #333a3d;
    --brand-blue: #2a86cc;
    --text-dark: #3a3d40;
    --divider: #4a4f52;
    --service-text: #ffffff;
  }
  html, body {
    margin: 0;
    width: 1200px;
    height: 930px;
    overflow: hidden;
    background: var(--backdrop);
  }
  .canvas { position: relative; width: 1200px; height: 930px; }
  .card {
    position: absolute;
    left: 278px;
    width: 645px;
    height: 368px;
    border-radius: 20px;
    overflow: hidden;
  }
  .card svg.wave { position: absolute; left: 0; top: 0; }
  .card-front { top: 76px; background: var(--card-white); }
  .card-back { top: 486px; background: var(--card-dark); }

  .brand-name {
    font-family: "Cinzel", serif;
    font-weight: 400;
    letter-spacing: 0.12em;
    white-space: nowrap;
    position: absolute;
  }
  .card-front .brand-name {
    left: 36px; top: 176px;
    font-size: 22px;
    color: var(--text-dark);
  }
  .divider {
    position: absolute;
    left: 311px; top: 102px;
    width: 1.5px; height: 160px;
    background: var(--divider);
  }
  .contact {
    position: absolute;
    left: 341px; top: 100px;
    font-family: "Work Sans", sans-serif;
    color: var(--text-dark);
    font-size: 16.5px;
    line-height: 20px;
  }
  .person-name {
    font-family: "Cinzel", serif;
    font-weight: 600;
    color: var(--brand-blue);
    font-size: 28px;
    line-height: 34px;
    margin: 0;
  }
  .person-title { margin: -2px 0 0; }
  .address { margin: 12px 0 0; }
  .links { list-style: none; padding: 0; margin: 8px 0 0; }
  .links li { display: flex; align-items: center; gap: 11px; }
  .links svg { width: 10px; height: 10px; flex: none; }
  .links .accent { color: var(--brand-blue); }

  .card-back .brand-name {
    left: 0; right: 0; top: 78px;
    text-align: center;
    font-size: 40px;
    color: var(--card-white);
  }
  .services {
    position: absolute;
    left: 0; right: 0; top: 176px;
    text-align: center;
    font-family: "Roboto Condensed", sans-serif;
  }
  .services h2 {
    margin: 0 0 6px;
    font-size: 24px;
    font-weight: 700;
    color: var(--brand-blue);
  }
  .services p {
    margin: 0;
    font-size: 17.5px;
    line-height: 21.6px;
    color: var(--service-text);
  }
</style>
</head>
<body>
<div class="canvas">

  <section class="card card-front">
    <svg class="wave" width="645" height="368" viewBox="0 0 645 368">
      <defs>
        <linearGradient id="frontStroke" x1="0" x2="1">
          <stop offset="0" stop-color="#2a86cc"/>
          <stop offset="0.55" stop-color="#8fbde3"/>
          <stop offset="1" stop-color="#ffffff"/>
        </linearGradient>
      </defs>
      <path d="M0 316 C80 336 140 352 220 346 C300 340 360 318 420 318 C500 318 580 340 645 352 L645 368 L0 368 Z" fill="#353b3e"/>
      <path d="M0 310 C80 332 140 346 220 340 C300 334 360 312 420 312 C500 312 580 332 645 348 L645 352 C580 340 500 320 420 320 C360 320 300 342 220 348 C140 354 80 336 0 316 Z" fill="url(#frontStroke)"/>
    </svg>

    <div class="brand-name">Lark Hollow Yard</div>
    <div class="divider"></div>

    <div class="contact">
      <h1 class="person-name">Dennis Harlow</h1>
      <p class="person-title">President</p>
      <p class="address">4817 Birchwell Meadow Lane SE,<br>Grand Rapids, Michigan 49582</p>
      <ul class="links">
        <li>
          <svg viewBox="0 0 10 10" aria-hidden="true"><path d="M2 1 L4 1 L4.5 3 L3.3 3.8 C3.8 5 4.9 6.1 6.2 6.7 L7 5.5 L9 6 L9 8 C5 8.5 1.5 5 2 1 Z" fill="none" stroke="#2a86cc" stroke-width="1"/></svg>
          <span>616.555.0187</span>
        </li>
        <li>
          <svg viewBox="0 0 10 10" aria-hidden="true"><rect x="0.7" y="2" width="8.6" height="6" fill="none" stroke="#2a86cc" stroke-width="1"/><path d="M0.7 2 L5 5.5 L9.3 2" fill="none" stroke="#2a86cc" stroke-width="1"/></svg>
          <span>company@larkhollowyard.com</span>
        </li>
        <li>
          <svg viewBox="0 0 10 10" aria-hidden="true"><circle cx="5" cy="5" r="4.2" fill="none" stroke="#2a86cc" stroke-width="0.9"/><ellipse cx="5" cy="5" rx="1.8" ry="4.2" fill="none" stroke="#2a86cc" stroke-width="0.8"/><path d="M0.8 5 H9.2" stroke="#2a86cc" stroke-width="0.8"/></svg>
          <span>www.<span class="accent">larkhollowyard</span>.com</span>
        </li>
      </ul>
    </div>
  </section>

  <section class="card card-back">
    <svg class="wave" width="645" height="368" viewBox="0 0 645 368">
      <defs>
        <linearGradient id="backBand" x1="0" x2="1">
          <stop offset="0" stop-color="#2a86cc"/>
          <stop offset="1" stop-color="#5a8fa3"/>
        </linearGradient>
        <linearGradient id="backStroke" x1="0" x2="1">
          <stop offset="0" stop-color="#2a86cc"/>
          <stop offset="0.6" stop-color="#2d6d9c"/>
          <stop offset="1" stop-color="#333a3d"/>
        </linearGradient>
      </defs>
      <path d="M0 306 C90 330 170 342 250 336 C340 330 400 310 470 310 C550 310 610 322 645 330 L645 368 L0 368 Z" fill="url(#backStroke)"/>
      <path d="M0 310 C90 336 170 348 250 342 C340 336 400 318 470 318 C550 318 610 330 645 338 L645 342 C610 336 550 324 470 324 C400 324 340 342 250 348 C170 354 90 342 0 318 Z" fill="#2b3134"/>
      <path d="M0 318 C90 342 170 354 250 348 C340 342 400 324 470 324 C550 324 610 336 645 342 L645 368 L0 368 Z" fill="url(#backBand)"/>
    </svg>

    <div class="brand-name">Lark Hollow Yard</div>

    <div class="services">
      <h2>SERVICES OFFERED...</h2>
      <p>Landscape design &amp; installation | Professional lawn maintenance<br>
      Spring &amp; fall leaf cleanup | Irrigation system installation &amp; maintenance<br>
      Snowplowing, Fertilizer &amp; weed control | Tree maintenance and removal<br>
      Landscape bed maintenance</p>
    </div>
  </section>

</div>
</body>
</html>
```